project - Plume Den

Dear designers, I'm Looking for an appealing new business card design to represent us for our new e-cigarette store: The Plume Den. Knowledgeable and friendly staff we aim for superior customer service with a positive atmosphere. Classic feel with modern touch is what we are aiming for . Lime green font and grey back round is the original color scheme but we are flexible and open to suggestions. I added some doodles to show you where my mind is at. address: 4826 97 St SW Edmonton, AB (inside the grand bazaar hall)web: theplumeden.com email: info@theplumeden.com phone : 780.555.6147 Thanks and am looking forward to seeing your creative , fresh and innovative designs.
Good luck everybody!
Gavin
lime green and charcoal grey please. thanks
Business
The Plume Den

```html
<!DOCTYPE html>
<html lang="en">
<head>
<meta charset="utf-8">
<title>The Plume Den – Business Card</title>
<link href="https://fonts.googleapis.com/css2?family=Roboto:wght@400&display=swap" rel="stylesheet">
<style>
  :root {
    --stage: #e9e7e3;
    --charcoal-deep: #1c1f21;
    --charcoal: #2b2f32;
    --charcoal-light: #3d4246;
    --band: #4a5054;
    --lime: #6fd24a;
    --card-shadow: rgba(0, 0, 0, 0.28);
  }
  * { box-sizing: border-box; margin: 0; padding: 0; }
  html, body {
    width: 1200px;
    height: 900px;
    overflow: hidden;
    background: var(--stage);
  }
  .stage {
    position: relative;
    width: 1200px;
    height: 900px;
  }
  .card {
    position: absolute;
    width: 560px;
    height: 320px;
    border-radius: 8px;
    overflow: hidden;
    box-shadow: 0 14px 30px var(--card-shadow);
  }
  .card--front { left: 110px; top: 100px; }
  .card--back  { left: 530px; top: 480px; }

  .front-texture {
    position: absolute;
    inset: 0;
    background: radial-gradient(ellipse at 40% 30%, var(--charcoal-light) 0%, var(--charcoal) 55%, var(--charcoal-deep) 100%);
  }
  .brand-name {
    position: absolute;
    left: 0; right: 0;
    text-align: center;
    font-family: "Roboto", Arial, sans-serif;
    font-weight: 400;
    color: var(--lime);
    white-space: nowrap;
    letter-spacing: 1px;
  }
  .card--front .brand-name {
    top: 136px;
    font-size: 38px;
    line-height: 48px;
  }

  .back-surface {
    position: absolute;
    inset: 0;
    background: linear-gradient(180deg, var(--charcoal) 0%, var(--charcoal-deep) 100%);
  }
  .back-band {
    position: absolute;
    left: 0; right: 0; top: 0;
    height: 122px;
    background: linear-gradient(180deg, var(--band) 0%, var(--charcoal-light) 100%);
  }
  .card--back .brand-name {
    top: 58px;
    font-size: 26px;
    line-height: 34px;
  }
  .contact {
    position: absolute;
    left: 200px;
    top: 150px;
    font-family: "Roboto", Arial, sans-serif;
    font-size: 13px;
    line-height: 16px;
    color: var(--lime);
    list-style: none;
  }
  .contact__address { margin-bottom: 24px; letter-spacing: 0.3px; }
  .contact__item {
    display: flex;
    align-items: center;
    gap: 10px;
    margin-left: 80px;
    margin-bottom: 13px;
  }
  .contact__icon { width: 13px; height: 13px; flex: none; }
</style>
</head>
<body>
<main class="stage">
  <section class="card card--front">
    <div class="front-texture" role="img" aria-label="Fine charcoal dot halftone texture across the card"></div>
    <p class="brand-name">The Plume Den</p>
  </section>

  <section class="card card--back">
    <div class="back-surface"></div>
    <div class="back-band"></div>
    <p class="brand-name">The Plume Den</p>
    <ul class="contact">
      <li class="contact__address">4826 97 St SW Edmonton, AB</li>
      <li class="contact__item">
        <svg class="contact__icon" viewBox="0 0 24 24" aria-hidden="true"><path fill="#6fd24a" d="M6.6 10.8a15.1 15.1 0 0 0 6.6 6.6l2.2-2.2a1 1 0 0 1 1-.25 11.4 11.4 0 0 0 3.6.57 1 1 0 0 1 1 1V20a1 1 0 0 1-1 1A17 17 0 0 1 3 4a1 1 0 0 1 1-1h3.5a1 1 0 0 1 1 1c0 1.25.2 2.45.57 3.57a1 1 0 0 1-.25 1z"/></svg>
        <span>780.555.6147</span>
      </li>
      <li class="contact__item">
        <svg class="contact__icon" viewBox="0 0 24 24" aria-hidden="true"><rect x="2" y="5" width="20" height="14" rx="1.5" fill="#6fd24a"/><path d="M3 6l9 7 9-7" fill="none" stroke="#1c1f21" stroke-width="1.8"/></svg>
        <span>info@theplumeden.com</span>
      </li>
      <li class="contact__item">
        <svg class="contact__icon" viewBox="0 0 24 24" aria-hidden="true"><circle cx="12" cy="12" r="10" fill="none" stroke="#6fd24a" stroke-width="2"/><ellipse cx="12" cy="12" rx="4" ry="10" fill="none" stroke="#6fd24a" stroke-width="1.6"/><path d="M2 12h20" stroke="#6fd24a" stroke-width="1.6"/></svg>
        <span>theplumeden.com</span>
      </li>
    </ul>
  </section>
</main>
</body>
</html>
```